'Edge of the Creek' flyer design

We need a flyer designed to promote our accommodation and boat hire. We have a rustic style self contained accommodation. Please view on Rent a Cove, NZ ID #581037 this has all the photos and information that might be needed. Feel free to contact me if you need/want any of them sending through. We would like to add 1 photo of the boats though so need a space for them. This is a new venture. The only thing we don't have is prices so not sure if we actually put that on or not? Would be nice to add a couple of peoples 'comments' about the place.
Look forward to see what you come up with.
HAS TO BE A6

Thanks Tessa

Target Market(s)

Holiday makers, family, fishermen.

Industry/Entity Type

Accommodation

Requirements
Must have
• Self Contained Accommodation.
Boat Hire, 2 x RM615 with 40hp Korvath outboards, live bait tank, 4 people max. Launch and retrieve if needed.
Vacation Nests ID #4127, Rent a Cove ID #581037
Ph 07 5231 907
Mob 027 4813 562
Must have bar photo and pizza bar photo.And boat photo
Nice to have
• Fishing photos together and accommodation photos together. Maybe 1 side each.
Some comments would be nice if you think appropriate.

```html
<!DOCTYPE html>
<html lang="en">
<head>
<meta charset="utf-8">
<title>Edge of the Creek – Flyer</title>
<link rel="stylesheet" href="https://fonts.googleapis.com/css2?family=Fira+Sans:wght@700&family=Cinzel:wght@400;600&family=Noto+Sans:wght@700&display=swap">
<style>
  :root{
    --page:#e6e6e6;
    --paper:#ffffff;
    --green:#6a9a3c;
    --blue:#2f63a8;
    --brown:#7b4a32;
    --band:#262a27;
    --maroon:#7a1218;
    --email:#8fc05a;
    --sea-text:#1a6fb0;
    --photo-frame:#ffffff;
  }
  *{box-sizing:border-box;margin:0;padding:0}
  html,body{width:849px;height:1200px;overflow:hidden;background:var(--page)}
  .flyer{position:absolute;left:85px;width:680px;height:478px;background:var(--paper);overflow:hidden;box-shadow:0 2px 8px rgba(0,0,0,.25)}
  .flyer--front{top:58px}
  .flyer--back{top:640px}
  .shapes{position:absolute;inset:0;width:100%;height:100%}
  .title{position:absolute;font-family:"Fira Sans",sans-serif;font-weight:700;color:var(--brown);font-size:35px;letter-spacing:-.5px;white-space:nowrap}
  .subtitle{position:absolute;font-family:"Cinzel",serif;color:var(--brown);white-space:nowrap;line-height:1}
  .features{position:absolute;left:38px;top:125px;width:556px;list-style:none;font-family:"Noto Sans",sans-serif;font-weight:700;font-size:11.6px;line-height:16px;color:#1e2a1e}
  .features li{position:relative;padding-left:15px;margin-bottom:1px;text-align:justify}
  .features li::before{content:"";position:absolute;left:0;top:4px;width:9px;height:9px;border-radius:50%;background:var(--green)}
  .photo{position:absolute;border:3px solid var(--photo-frame);box-shadow:0 2px 6px rgba(0,0,0,.4)}
  .photo--bar{left:38px;top:226px;width:294px;height:164px;background:linear-gradient(160deg,#9dbf7a,#4f7a3a 55%,#7a6a52)}
  .photo--pizza{left:345px;top:226px;width:292px;height:164px;background:linear-gradient(150deg,#8b8f86,#6c5a44 50%,#b7773f)}
  .band-text{position:absolute;font-family:"Noto Sans",sans-serif;font-weight:700;white-space:nowrap}
  .email{left:290px;top:402px;width:390px;text-align:center;font-size:20px;color:var(--email);line-height:29px}
  .address{right:42px;top:439px;font-size:18.5px;color:var(--maroon)}
  .hire-details{position:absolute;left:27px;top:103px;width:352px;font-family:"Noto Sans",sans-serif;font-weight:700;font-size:18.6px;line-height:25px;color:var(--sea-text);text-align:justify}
  .oval{position:absolute;border-radius:50%;border:3px solid #1c1c1c;box-shadow:0 2px 6px rgba(0,0,0,.45)}
  .oval--boats{left:390px;top:75px;width:256px;height:162px;background:linear-gradient(160deg,#7c7a72,#a9a69c 50%,#6d6a62)}
  .oval--anglers{left:361px;top:224px;width:240px;height:146px;background:linear-gradient(160deg,#5f7c48,#3a3f3a 55%,#8a9aa0)}
  .oval--kids{left:60px;top:302px;width:172px;height:112px;background:linear-gradient(150deg,#2a2a2a,#b85a4a 55%,#2e2e2e)}
  .oval--catch{left:219px;top:285px;width:198px;height:128px;background:linear-gradient(150deg,#6fa0c4,#3a3c3e 55%,#9fb3bf)}
  .phones{left:155px;top:416px;width:527px;font-size:20px;line-height:28px;color:#fff}
  .phones .label{color:var(--email);font-weight:400}
  .phones .ph{position:absolute;left:102px}
  .phones .mob{position:absolute;left:344px}
  .ref{right:74px;top:449px;font-size:14.5px;color:var(--maroon)}
</style>
</head>
<body>

<section class="flyer flyer--front">
  <svg class="shapes" viewBox="0 0 680 478" preserveAspectRatio="none">
    <rect role="img" aria-label="Faded backdrop photo of the bush property with play fort and lawn" x="0" y="0" width="680" height="478" fill="url(#frontBackdrop)"/>
    <defs>
      <linearGradient id="frontBackdrop" x1="0" y1="0" x2="1" y2="1">
        <stop offset="0" stop-color="#f6f7f3"/>
        <stop offset=".5" stop-color="#e3e7dc"/>
        <stop offset="1" stop-color="#c9cfc2"/>
      </linearGradient>
    </defs>
    <path d="M430 0 H680 V270 C650 150 570 50 430 0 Z" fill="var(--green)"/>
    <path d="M430 0 C570 50 650 150 680 270" fill="none" stroke="#fff" stroke-width="5"/>
    <path d="M0 230 C40 340 160 430 260 478 H0 Z" fill="var(--green)"/>
    <path d="M0 230 C40 340 160 430 260 478" fill="none" stroke="#fff" stroke-width="5"/>
    <rect x="218" y="402" width="462" height="29" fill="var(--band)"/>
    <path d="M218 402 C240 410 255 420 262 431 H218 Z" fill="var(--green)"/>
    <rect x="262" y="431" width="418" height="47" fill="#fff"/>
    <path d="M218 431 C240 445 250 460 262 478 H262 V431 Z" fill="#fff"/>
  </svg>

  <h1 class="title" style="left:41px;top:18px">'Edge of the Creek'</h1>
  <p class="subtitle" style="left:120px;width:230px;text-align:right;top:64px;font-size:19px">COROMANDEL TOWN</p>
  <p class="subtitle" style="left:38px;top:86px;font-size:15.5px;font-weight:600">SELF CONTAINED ACCOMMODATION</p>

  <ul class="features">
    <li>2 minute drive to town, 6 private acres , kids will enjoy native bush walks, large meandering creeks, rope climb, flying fox etc.</li>
    <li>Outdoor bar and BBQ area, sheltered fish filleting facilities and big smokehouse. Safe boat parking.</li>
    <li>All linen provided (incl. towels,tea towels,duvets,pillows and sheets) No extra charge for cleaning.</li>
  </ul>

  <div class="photo photo--bar" role="img" aria-label="Photo of the rustic outdoor bar shelter among native bush"></div>
  <div class="photo photo--pizza" role="img" aria-label="Photo of the pizza bar with wood-fired oven and timber table"></div>

  <p class="band-text email">tessa.ken@kiwimail.co.nz</p>
  <p class="band-text address">212 Harbour Lane, Coromandel Town.</p>
</section>

<section class="flyer flyer--back">
  <svg class="shapes" viewBox="0 0 680 478" preserveAspectRatio="none">
    <defs>
      <linearGradient id="seaBackdrop" x1="0" y1="0" x2="0" y2="1">
        <stop offset="0" stop-color="#f3f5f6"/>
        <stop offset=".32" stop-color="#d7e2ea"/>
        <stop offset=".45" stop-color="#7fb2d2"/>
        <stop offset="1" stop-color="#3f8fc0"/>
      </linearGradient>
    </defs>
    <rect role="img" aria-label="Backdrop photo of the harbour with a hire boat and anglers on the water" x="0" y="0" width="680" height="478" fill="url(#seaBackdrop)"/>
    <path d="M420 0 H680 V300 C670 160 590 50 420 0 Z" fill="var(--blue)"/>
    <path d="M420 0 C590 50 670 160 680 300" fill="none" stroke="#fff" stroke-width="5"/>
    <path d="M0 240 C30 350 120 430 210 478 H0 Z" fill="var(--blue)"/>
    <path d="M0 240 C30 350 120 430 210 478" fill="none" stroke="#fff" stroke-width="5"/>
    <rect x="155" y="416" width="525" height="28" fill="var(--band)"/>
    <rect x="205" y="444" width="475" height="34" fill="#fff"/>
    <path d="M155 444 C175 455 190 465 205 478 V444 Z" fill="#fff"/>
  </svg>

  <h1 class="title" style="left:41px;top:16px">'Harbourside Boat Hire'</h1>
  <p class="subtitle" style="left:150px;width:256px;text-align:right;top:62px;font-size:19px">COROMANDEL TOWN</p>

  <p class="hire-details">Boat Hire, 2 x RM615 with 40hp Korvath outboards, live bait tank, 4 people max. Launch and retrieve if needed.</p>

  <div class="oval oval--boats" role="img" aria-label="Photo of the two hire boats on trailers in the shed"></div>
  <div class="oval oval--anglers" role="img" aria-label="Photo of three anglers holding their snapper catch"></div>
  <div class="oval oval--kids" role="img" aria-label="Photo of children holding a large snapper"></div>
  <div class="oval oval--catch" role="img" aria-label="Photo of a guest holding two fish by the water"></div>

  <p class="band-text phones"><span class="ph"><span class="label">Ph</span> 07 5231 907</span><span class="mob"><span class="label">Mob</span> 027 4813 562</span></p>
  <p class="band-text ref">Ref No; Vacation Nests #4127, Rent a Cove #581037</p>
</section>

</body>
</html>
```